Safety Consultancy focusing on developing exceptional Safety Leaders

I need a full but simple, modern, catchy website to drive business - my focus is on helping organizations to understand the impact that leaders have on safety performance and how they build the processes to make that happen. I already have great branding (logos) built through ArtisanHive and can provide all narrative to build out the pages

Target Market(s)

Focused internationally. Typical client has a fairly robust and mature safety culture yet lacks the focused effort to develop all levels of leadership in terms of managing safety. Exercising these competencies results in continued development of an organizations safety culture as well as improved safety performance

Industry/Entity Type

all

Coding

Coded - Design and coding required

Number of Pages Required

4 page

Font styles to use
Other font styles liked:
• to match my branding

Colors
0054AA
0677BA
7BADD7
CADEEF
E8F1F8

Requirements
Must have
• Must utilize my current branding, logo, etc. I want to have a page outlining clearly my vision - which I will add to my uploads as we move forward. I need to have a page listing my extensive and unique experience as well as successes
Nice to have
• Want to leave it up to designers - but needs to be simple and easily navigable - hope to have a resource page that I can update myself with safety resource info, reports, etc.

```html
<!DOCTYPE html>
<html lang="en">
<head>
<meta charset="utf-8">
<title>Halvern Safety Partners</title>
<link rel="stylesheet" href="https://fonts.googleapis.com/css2?family=Ubuntu:wght@400;500;700&family=Lato:wght@400;700&display=swap">
<style>
:root{
  --ink:#0a2f63;
  --brand:#0054aa;
  --brand-mid:#0677ba;
  --brand-soft:#7badd7;
  --brand-light:#cadeef;
  --brand-mist:#e8f1f8;
  --brand-deep:#003f80;
  --band-dark:#00346b;
  --card-bg:#f4f8fb;
  --text:#2b2b2b;
  --muted:#7f8a99;
  --white:#ffffff;
  --orange:#f29a2e;
}
*{box-sizing:border-box;margin:0;padding:0}
html,body{width:1200px;height:4189px;overflow:hidden;background:var(--white)}
body{font-family:"Lato",sans-serif;color:var(--text)}
.page{position:relative;width:1200px;height:4189px;overflow:hidden}
.abs{position:absolute}
.h-font{font-family:"Ubuntu",sans-serif}

/* header */
.topbar{left:385px;top:0;width:815px;height:32px;background:var(--brand-deep);display:flex;font-size:11px;color:var(--white)}
.topbar div{display:flex;align-items:center;gap:8px}
.topbar .phone{width:207px;justify-content:center;font-weight:700}
.topbar .appt{width:237px;justify-content:center;background:var(--brand-mid);text-transform:uppercase}
.topbar .addr{padding-left:30px}
.brand{left:128px;top:28px;display:flex;align-items:center;gap:10px}
.brand .mark{width:34px;height:34px;border-radius:50%;background:var(--brand-light)}
.brand .name{font-family:"Ubuntu",sans-serif;font-weight:500;font-size:30px;color:var(--ink);line-height:1}
.brand .sub{font-family:"Ubuntu",sans-serif;font-size:11px;color:var(--ink);line-height:1.1}
.nav{top:61px;font-size:11px;font-weight:700;color:#333}
.nav span{position:absolute;white-space:nowrap}
.btn-outline{left:930px;top:52px;width:118px;height:32px;border:2px solid var(--brand);border-radius:5px;color:var(--brand);font-size:11px;display:flex;align-items:center;justify-content:center}

/* hero */
.hero-photo{left:0;top:96px;width:1200px;height:680px;background:linear-gradient(90deg,#f5f8fb 0%,#eaf1f7 35%,#b3c8db 60%,#8aa6c0 100%)}
.kicker{left:124px;top:265px;font-size:20px;letter-spacing:5px;font-weight:700;color:#111}
.hero-title{left:118px;top:305px;font-size:70px;font-weight:700;color:var(--ink);font-family:"Ubuntu",sans-serif;white-space:nowrap}
.hero-rule{left:122px;top:400px;width:500px;height:3px;background:var(--brand)}
.hero-copy{left:124px;top:425px;width:520px;font-size:16px;line-height:28px;color:#222}
.pill{top:510px;height:42px;border-radius:21px;color:var(--white);font-weight:700;font-size:14px;display:flex;align-items:center;justify-content:center}

/* section labels */
.label{font-size:13px;color:var(--brand-mid);text-transform:uppercase;text-align:center;width:1200px;left:0}
.label span{border-bottom:1px solid currentColor;padding-bottom:2px}
.heading{width:1200px;left:0;text-align:center;font-family:"Ubuntu",sans-serif;font-weight:700;font-size:42px;color:var(--ink)}
.accent{color:var(--brand-mid)}

/* about */
.about-photo{left:120px;top:974px;width:495px;height:338px;border-radius:8px;background:linear-gradient(135deg,#c9d6e3,#7b8fa3 55%,#4f5b66)}
.about-card{left:562px;top:998px;width:516px;height:306px;background:var(--card-bg);border-radius:6px;padding:48px 30px 0 36px}
.about-card h3{font-family:"Ubuntu",sans-serif;font-weight:500;font-size:19px;color:#222;margin-bottom:14px}
.about-card p{font-size:12px;line-height:19px;color:var(--muted);margin-bottom:10px}
.btn-sq{height:40px;background:var(--brand);color:var(--white);font-weight:700;font-size:14px;border-radius:2px;display:flex;align-items:center;justify-content:center;gap:14px}

/* services */
.services{left:0;top:1416px;width:1200px;height:556px;background:linear-gradient(90deg,var(--brand-deep),var(--band-dark) 50%,var(--brand-deep))}
.svc{top:1605px;width:303px;height:227px;color:var(--white)}
.svc .ttl{font-family:"Ubuntu",sans-serif;font-weight:700;font-size:16px;white-space:nowrap}
.svc .txt{font-size:13px}

/* steps */
.steps{left:0;top:1972px;width:1200px;height:498px;background:var(--brand-mist)}
.step{top:2170px;width:230px;text-align:center}
.step .ring{position:absolute;left:55px;top:0;width:120px;height:120px;border-radius:50%;border:2px solid var(--brand-soft);background:var(--white)}
.step .core{position:absolute;left:10px;top:10px;width:96px;height:96px;border-radius:50%;background:var(--brand-deep);display:flex;align-items:center;justify-content:center}
.step .num{position:absolute;left:158px;top:47px;width:28px;height:28px;border-radius:50%;background:var(--brand-mid);color:var(--white);font-size:11px;font-weight:700;display:flex;align-items:center;justify-content:center;border:2px solid var(--white)}
.step h4{position:absolute;top:143px;width:230px;font-family:"Ubuntu",sans-serif;font-weight:500;font-size:18px;color:#222}
.step p{position:absolute;top:172px;left:15px;width:200px;font-size:13px;line-height:21px;color:var(--muted)}

/* tailored */
.tailored-photo{left:0;top:2470px;width:1200px;height:576px;background:linear-gradient(90deg,#e3eaf1,#c8d4df 30%,#6b7b8c 60%)}
.feature{left:630px;width:440px;display:flex;gap:16px;align-items:center;color:var(--white)}
.feature .ic{width:62px;height:62px;border-radius:50%;background:var(--white);display:flex;align-items:center;justify-content:center;flex:none}
.feature b{font-family:"Ubuntu",sans-serif;font-size:19px;display:block;margin-bottom:4px;font-weight:500}
.feature span{font-size:13px;color:var(--brand-light)}

/* testimonials */
.avatar{border-radius:50%;background:linear-gradient(135deg,#c7b7a8,#6d5d55)}
.quote{left:305px;top:3382px;width:590px;text-align:center;font-size:15px;line-height:23px;color:#222}

/* footer */
.foot-nav{top:3952px;font-size:14px;color:var(--white)}
.foot-nav span{position:absolute;white-space:nowrap}
.contact{top:4040px;display:flex;align-items:center;gap:12px;color:var(--white);font-size:12px}
.contact .ic{width:56px;height:56px;border-radius:50%;border:1px solid rgba(255,255,255,.6);display:flex;align-items:center;justify-content:center}
.bottombar{left:0;top:4130px;width:1200px;height:59px;background:var(--brand);color:var(--white);font-size:12px}
.social{top:4148px;width:24px;height:24px;border:1px solid var(--white);border-radius:3px}
</style>
</head>
<body>
<div class="page">

  <!-- header -->
  <div class="abs topbar">
    <div class="phone"><svg width="14" height="14" viewBox="0 0 24 24" fill="none" stroke="#fff" stroke-width="2"><path d="M5 3h4l2 5-3 2a11 11 0 006 6l2-3 5 2v4a2 2 0 01-2 2A17 17 0 013 5a2 2 0 012-2z"/></svg>555 - 214 - 0387</div>
    <div class="appt"><svg width="14" height="14" viewBox="0 0 24 24" fill="none" stroke="#fff" stroke-width="2"><rect x="3" y="5" width="18" height="16" rx="2"/><path d="M3 10h18M8 3v4M16 3v4"/></svg>Request an appointment</div>
    <div class="addr"><svg width="12" height="14" viewBox="0 0 24 28" fill="none" stroke="#fff" stroke-width="2"><path d="M12 26s9-9 9-15a9 9 0 00-18 0c0 6 9 15 9 15z"/><circle cx="12" cy="11" r="3"/></svg>88 Harbor Lane, Suite 4</div>
  </div>
  <div class="abs brand">
    <div class="mark"></div>
    <div><div class="name">Halvern</div><div class="sub">Safety Partners</div></div>
  </div>
  <div class="abs nav" style="left:0;width:1200px">
    <span style="left:395px">Home</span><span style="left:470px">About Us</span><span style="left:545px">Solutions</span><span style="left:620px">Projects</span><span style="left:726px">Our Team</span>
  </div>
  <div class="abs btn-outline">CONTACT US</div>

  <!-- hero -->
  <div class="abs hero-photo" role="img" aria-label="Photo of safety leaders in hard hats reviewing plans on a factory floor"></div>
  <svg class="abs" style="left:0;top:690px" width="1200" height="100" viewBox="0 0 1200 100" preserveAspectRatio="none">
    <path d="M0 40 C300 0 600 30 900 45 C1050 52 1150 40 1200 10 L1200 100 L0 100Z" fill="#fff"/>
    <path d="M0 40 C300 0 600 30 900 45 C1050 52 1150 40 1200 10 L1200 50 C1150 80 1050 70 900 62 C600 45 300 20 0 45Z" fill="#0677ba"/>
  </svg>
  <div class="abs kicker">Experts in</div>
  <div class="abs hero-title">Safety Leadership</div>
  <div class="abs hero-rule"></div>
  <p class="abs hero-copy">We develop leaders at every level who build the processes that drive safety culture and performance</p>
  <div class="abs pill" style="left:124px;width:146px;background:var(--brand)">LEARN MORE</div>
  <div class="abs pill" style="left:281px;width:179px;background:#111">REQUEST QUOTE</div>

  <!-- who we are -->
  <div class="abs label" style="top:845px"><span>Who we are</span></div>
  <h2 class="abs heading" style="top:880px">Your <span class="accent">Leaders</span>, Our Expertise</h2>
  <div class="abs about-photo" role="img" aria-label="Photo of a technician checking aircraft landing gear on the tarmac"></div>
  <div class="abs about-card">
    <h3>Building Leaders, Elevating Safety</h3>
    <p>Leaders shape safety performance. We help mature organizations understand that impact and develop every level of leadership, from frontline supervisors to executives, to manage safety with intent.</p>
    <p>Stronger leadership competencies mean a safety culture that keeps growing and results that keep improving.</p>
  </div>
  <div class="abs btn-sq" style="left:602px;top:1226px;width:136px">Contact us <svg width="16" height="12" viewBox="0 0 16 12" fill="none" stroke="#fff" stroke-width="1.5"><path d="M0 6h15M10 1l5 5-5 5"/></svg></div>

  <!-- services -->
  <div class="abs services"></div>
  <div class="abs label" style="top:1474px;color:#fff"><span>Our services</span></div>
  <h2 class="abs heading" style="top:1510px;color:#fff;font-weight:500">Services We Provide</h2>

  <div class="abs svc" style="left:120px;background:linear-gradient(160deg,#2f3640,#15191e)" role="img" aria-label="Photo of a supervisor reviewing stock in a warehouse"></div>
  <div class="abs svc" style="left:120px;text-align:center;padding:78px 30px 0">
    <div class="ttl">Leadership Assessments</div>
    <div class="txt" style="margin-top:6px;line-height:21px">Measure how your leaders influence safety at every level of the organization</div>
    <svg style="margin-top:10px" width="28" height="12" viewBox="0 0 28 12" fill="none" stroke="#fff" stroke-width="1.5"><path d="M0 6h27M21 1l6 5-6 5"/></svg>
  </div>
  <div class="abs svc" style="left:447px;background:linear-gradient(180deg,#8a949e,#4a5560 60%,#0f2f55)" role="img" aria-label="Photo of a team in hard hats reviewing a laptop on site"></div>
  <div class="abs svc" style="left:447px;background:none;display:flex;align-items:flex-end;padding:0 0 22px 36px;gap:14px">
    <svg width="30" height="30" viewBox="0 0 24 24" fill="none" stroke="#7badd7" stroke-width="1.6"><path d="M9 3l5 5-6 6-5-5z M3 21h18M8 17h8"/></svg>
    <div><div class="ttl">Safety Leader Coaching</div><div class="txt" style="margin-top:4px">Build core safety competencies</div></div>
  </div>
  <div class="abs svc" style="left:775px;background:linear-gradient(180deg,#6f6a5e,#363a40 60%,#0d2a4d)" role="img" aria-label="Photo of engineers inspecting a steel structure"></div>
  <div class="abs svc" style="left:775px;background:none;display:flex;align-items:flex-end;padding:0 0 22px 32px;gap:14px">
    <svg width="30" height="30" viewBox="0 0 24 24" fill="none" stroke="#7badd7" stroke-width="1.6"><path d="M12 2l3 6 7 1-5 5 1 7-6-3-6 3 1-7-5-5 7-1z"/></svg>
    <div><div class="ttl">Process Development</div><div class="txt" style="margin-top:4px">Systems that make it happen</div></div>
  </div>
  <div class="abs btn-sq" style="left:547px;top:1883px;width:136px;background:var(--brand-mid)">Contact us <svg width="16" height="12" viewBox="0 0 16 12" fill="none" stroke="#fff" stroke-width="1.5"><path d="M0 6h15M10 1l5 5-5 5"/></svg></div>

  <!-- steps -->
  <div class="abs steps"></div>
  <div class="abs label" style="top:2045px"><span>Steps to take</span></div>
  <h2 class="abs heading" style="top:2080px;font-weight:500"><span class="accent">Steps</span> To Take</h2>
  <div class="abs" style="left:340px;top:2229px;width:520px;height:2px;background:var(--brand-soft)"></div>
  <div class="abs step" style="left:166px">
    <div class="ring"><div class="core"><svg width="40" height="40" viewBox="0 0 24 24" fill="none" stroke="#fff" stroke-width="1.4"><path d="M9 3l5 5-6 6-5-5z M3 21h18M8 17h8"/></svg></div></div>
    <div class="num">01</div><h4>Contact Us to Start</h4><p>Tell us about your leaders, your culture and your safety goals</p>
  </div>
  <div class="abs step" style="left:482px">
    <div class="ring"><div class="core"><svg width="40" height="40" viewBox="0 0 24 24" fill="none" stroke="#fff" stroke-width="1.4"><path d="M9 3l5 5-6 6-5-5z M3 21h18M8 17h8"/></svg></div></div>
    <div class="num">02</div><h4>Get assigned an expert</h4><p>A seasoned consultant maps a plan for each leadership level</p>
  </div>
  <div class="abs step" style="left:796px">
    <div class="ring"><div class="core"><svg width="40" height="40" viewBox="0 0 24 24" fill="none" stroke="#fff" stroke-width="1.4"><path d="M9 3l5 5-6 6-5-5z M3 21h18M8 17h8"/></svg></div></div>
    <div class="num">03</div><h4>Start the Sessions</h4><p>Develop competencies and build the processes that last</p>
  </div>

  <!-- tailored -->
  <div class="abs tailored-photo" role="img" aria-label="Photo of a smiling business leader with arms crossed in a bright office"></div>
  <svg class="abs" style="left:0;top:2470px" width="1200" height="576" viewBox="0 0 1200 576">
    <path d="M380 0 H1200 V576 H660 Z" fill="#004a96" opacity="0.96"/>
  </svg>
  <div class="abs" style="left:635px;top:2564px;font-size:11px;color:var(--brand-soft);text-transform:uppercase">Who we are</div>
  <h2 class="abs h-font" style="left:635px;top:2595px;font-size:40px;line-height:48px;color:#fff;font-weight:500">Safety Leadership<br>Tailored for You</h2>
  <div class="abs feature" style="top:2709px"><div class="ic"><svg width="26" height="26" viewBox="0 0 24 24" fill="none" stroke="#0054aa" stroke-width="1.5"><path d="M9 3l5 5-6 6-5-5z M3 21h18M8 17h8"/></svg></div><div><b>Every Level of Leadership</b><span>From frontline supervisors to the executive team</span></div></div>
  <div class="abs feature" style="top:2789px"><div class="ic"><svg width="26" height="26" viewBox="0 0 24 24" fill="none" stroke="#0054aa" stroke-width="1.5"><path d="M4 15v-3a8 8 0 0116 0v3M4 14h3v6H4zM17 14h3v6h-3z"/></svg></div><div><b>Experienced Professionals</b><span>Proven results with mature safety cultures worldwide</span></div></div>
  <div class="abs feature" style="top:2872px"><div class="ic"><svg width="26" height="26" viewBox="0 0 24 24" fill="none" stroke="#0054aa" stroke-width="1.5"><path d="M12 2l3 6 7 1-5 5 1 7-6-3-6 3 1-7-5-5 7-1z"/></svg></div><div><b>Measurable Performance</b><span>Culture growth you can see in your safety results</span></div></div>

  <!-- testimonials -->
  <div class="abs label" style="top:3194px;font-size:17px"><span style="border:none">Testimonials</span></div>
  <h2 class="abs heading" style="top:3218px;font-size:32px;font-weight:500">What Our Clients are <span class="accent">Saying</span></h2>
  <div class="abs" style="left:567px;top:3303px;width:60px;height:60px;border-radius:50%;background:var(--brand-mid);display:flex;align-items:center;justify-content:center;color:#fff;font-family:Ubuntu,sans-serif;font-weight:700;font-size:44px;line-height:1;padding-top:18px">&rdquo;</div>
  <p class="abs quote">Our safety program was already strong, but our leaders did not see their part in it. Halvern changed that. Supervisors now own safety conversations, managers build the processes behind them, and our performance has improved every quarter since we began.</p>
  <div class="abs" style="left:0;width:1200px;top:3483px;text-align:center;font-size:13px;color:var(--orange)">Marcus Ellery</div>
  <div class="abs" style="left:0;width:1200px;top:3504px;text-align:center;font-size:11px;color:#222">Client</div>
  <div class="abs" style="left:547px;top:3543px;width:44px;height:44px;border-radius:50%;background:var(--ink);display:flex;align-items:center;justify-content:center"><svg width="18" height="14" viewBox="0 0 18 14" fill="none" stroke="#fff" stroke-width="1.6"><path d="M17 7H1M6 2L1 7l5 5"/></svg></div>
  <div class="abs" style="left:601px;top:3543px;width:44px;height:44px;border-radius:50%;background:var(--brand-mid);display:flex;align-items:center;justify-content:center"><svg width="18" height="14" viewBox="0 0 18 14" fill="none" stroke="#fff" stroke-width="1.6"><path d="M1 7h16M12 2l5 5-5 5"/></svg></div>

  <div class="abs avatar" style="left:241px;top:3303px;width:60px;height:60px" role="img" aria-label="Client portrait"></div>
  <div class="abs avatar" style="left:90px;top:3400px;width:100px;height:100px;background:linear-gradient(135deg,#5a6470,#1f252b)" role="img" aria-label="Client portrait"></div>
  <div class="abs avatar" style="left:263px;top:3418px;width:40px;height:40px" role="img" aria-label="Client portrait"></div>
  <div class="abs avatar" style="left:174px;top:3498px;width:80px;height:80px;background:linear-gradient(135deg,#6b4b3a,#2a2a2a)" role="img" aria-label="Client portrait"></div>
  <div class="abs avatar" style="left:893px;top:3308px;width:50px;height:50px" role="img" aria-label="Client portrait"></div>
  <div class="abs avatar" style="left:1004px;top:3348px;width:104px;height:104px;background:linear-gradient(135deg,#e6e2ea,#8a6d5a)" role="img" aria-label="Client portrait"></div>
  <div class="abs avatar" style="left:896px;top:3432px;width:56px;height:56px;background:linear-gradient(135deg,#dcd6d0,#9a7660)" role="img" aria-label="Client portrait"></div>
  <div class="abs avatar" style="left:996px;top:3500px;width:80px;height:80px;background:linear-gradient(135deg,#d8dbe0,#7d7a78)" role="img" aria-label="Client portrait"></div>

  <!-- footer -->
  <svg class="abs" style="left:0;top:3690px" width="1200" height="440" viewBox="0 0 1200 440" preserveAspectRatio="none">
    <path d="M0 60 C250 20 500 35 800 30 C1000 27 1120 10 1200 0 V440 H0Z" fill="#0677ba"/>
    <path d="M0 90 C250 45 500 60 800 55 C1000 52 1120 38 1200 30 V440 H0Z" fill="#003f80"/>
  </svg>
  <div class="abs" style="left:0;top:3840px;width:1200px;display:flex;justify-content:center;align-items:center;gap:14px;color:#fff">
    <div style="width:40px;height:40px;border-radius:50%;background:var(--brand-light)"></div>
    <div><div class="h-font" style="font-size:44px;font-weight:500;line-height:1">Halvern</div><div class="h-font" style="font-size:16px">Safety Partners</div></div>
  </div>
  <div class="abs foot-nav" style="left:0;width:1200px">
    <span style="left:296px">HOME</span><span style="left:390px">SERVICES</span><span style="left:496px">ABOUT US</span><span style="left:615px">TESTIMONIALS</span><span style="left:765px">BLOG</span>
  </div>
  <div class="abs" style="left:141px;top:4000px;width:919px;height:1px;background:rgba(255,255,255,.4)"></div>
  <div class="abs" style="left:398px;top:4030px;width:1px;height:60px;background:rgba(255,255,255,.4)"></div>
  <div class="abs" style="left:718px;top:4030px;width:1px;height:60px;background:rgba(255,255,255,.4)"></div>
  <div class="abs contact" style="left:141px"><div class="ic"><svg width="28" height="28" viewBox="0 0 24 24" fill="none" stroke="#fff" stroke-width="1.2"><circle cx="12" cy="12" r="9"/><path d="M3 12h18M12 3c3 3 3 15 0 18M12 3c-3 3-3 15 0 18"/></svg></div><div style="line-height:18px">123, Building Name, Street<br>City, State XY 123456</div></div>
  <div class="abs contact" style="left:474px"><div class="ic"><svg width="26" height="26" viewBox="0 0 24 24" fill="none" stroke="#fff" stroke-width="1.2"><rect x="7" y="2" width="10" height="20" rx="2"/><path d="M11 18h2"/></svg></div><div style="line-height:17px"><span style="font-size:14px">PHONE</span><br>(555) 214 0388</div></div>
  <div class="abs contact" style="left:796px"><div class="ic"><svg width="26" height="26" viewBox="0 0 24 24" fill="none" stroke="#fff" stroke-width="1.2"><rect x="3" y="6" width="18" height="13" rx="1"/><path d="M3 7l9 7 9-7"/></svg></div><div style="line-height:17px"><span style="font-size:14px">EMAIL</span><br>hello@halvernsafety.com</div></div>
  <div class="abs bottombar"><span class="abs" style="left:147px;top:22px">Halvern</span></div>
  <div class="abs social" style="left:932px"></div>
  <div class="abs social" style="left:966px"></div>
  <div class="abs social" style="left:1000px"></div>
  <div class="abs social" style="left:1034px"></div>

</div>
</body>
</html>
```